BrightLane Real Estate Sign

We are in the process of rebranding our business and need a new For Sale \ Sold sign.
We're a prestige real estate agency and therefore require a really stylish sign.
I've uploaded the following files
1. The new company logo
2. "sample sign.jpg" which shows the type of sign we would like. It is a metal sign with a top panel and bottom panel.
3. Our previous sign "previous sign.jpg" if you're interested in seeing it.
The sign must be black with white text.
Our thoughts are that the top panel (refer to sample sign) would contain the text "For Sale" or "Sold". These would be two separate panels which are interchangeable and could be screwed in place.
The bottom panel would not contain any photos like the sample. However, it may contain our logo and my contact details etc.
The sign is 900mm wide x 1200mm high.
My details are:
Name: Desmond Harlow
Web: www.blrealestate.com.au
Email: sales@blrealestate.com.au
Phone: 0491 836 205

```html
<!DOCTYPE html>
<html lang="en">
<head>
<meta charset="utf-8">
<title>BrightLane Real Estate – For Sale Sign</title>
<link href="https://fonts.googleapis.com/css2?family=Arimo:wght@700&family=Open+Sans:wght@400;600;700&display=swap" rel="stylesheet">
<style>
  :root {
    --page-bg: #ffffff;
    --sign-black: #000000;
    --panel-red: #7a0f1a;
    --sign-white: #ffffff;
  }
  html, body {
    margin: 0;
    padding: 0;
    width: 1200px;
    height: 1000px;
    overflow: hidden;
    background: var(--page-bg);
  }
  .canvas {
    position: relative;
    width: 1200px;
    height: 1000px;
  }
  .sign {
    position: absolute;
    left: 268px;
    top: 58px;
    width: 664px;
    height: 884px;
    background: var(--sign-black);
    color: var(--sign-white);
    text-align: center;
  }
  .status-panel {
    height: 160px;
    background: var(--panel-red);
    display: flex;
    align-items: center;
    justify-content: center;
  }
  .status-panel__title {
    margin: 0;
    font-family: "Arimo", Arial, sans-serif;
    font-weight: 700;
    font-size: 90px;
    letter-spacing: 1px;
    line-height: 1;
    padding-top: 4px;
  }
  .agent {
    position: absolute;
    left: 0;
    right: 0;
    top: 388px;
  }
  .agent__name {
    margin: 0;
    font-family: "Arimo", Arial, sans-serif;
    font-weight: 700;
    font-size: 49px;
    line-height: 1;
    letter-spacing: 0.5px;
  }
  .agent__phone {
    margin: 12px 0 0;
    font-family: "Arimo", Arial, sans-serif;
    font-weight: 700;
    font-size: 82px;
    line-height: 1;
    letter-spacing: -1px;
  }
  .agent__email {
    margin: 10px 0 0;
    font-family: "Open Sans", Arial, sans-serif;
    font-weight: 400;
    font-size: 34px;
    line-height: 1.1;
  }
  .agent__web {
    position: absolute;
    left: 0;
    right: 0;
    top: 614px;
    margin: 0;
    font-family: "Open Sans", Arial, sans-serif;
    font-weight: 400;
    font-size: 27px;
    line-height: 1;
  }
  .brand {
    position: absolute;
    left: 0;
    right: 0;
    top: 760px;
    display: flex;
    align-items: center;
    justify-content: center;
    gap: 18px;
  }
  .brand__mark {
    width: 40px;
    height: 40px;
    background: var(--sign-white);
  }
  .brand__name {
    font-family: "Open Sans", Arial, sans-serif;
    font-weight: 700;
    font-size: 46px;
    line-height: 1;
  }
</style>
</head>
<body>
  <main class="canvas">
    <section class="sign" aria-label="BrightLane Real Estate for sale sign">
      <header class="status-panel">
        <h1 class="status-panel__title">FOR SALE</h1>
      </header>

      <div class="agent">
        <p class="agent__name">DESMOND HARLOW</p>
        <p class="agent__phone">0491 836 205</p>
        <p class="agent__email">sales@blrealestate.com.au</p>
      </div>

      <p class="agent__web">www.blrealestate.com.au</p>

      <div class="brand">
        <span class="brand__mark" aria-hidden="true"></span>
        <span class="brand__name">BrightLane Real Estate</span>
      </div>
    </section>
  </main>
</body>
</html>
```